Need a clever and fun book cover design for a new, fresh and different kind of environmental movement. I have a logo that I like and the title is Sing Along Harbor Weavers. I would like to create a book cover design so it includes the logo that I have uploaded for you.

Target Market(s)

My ideal audience are medium to large landowners located around shale oil and gas "plays" in the US

Requirements
Must have
• Would like to have a drilling rig in the back ground off in the distance.

```html
<!DOCTYPE html>
<html lang="en">
<head>
<meta charset="utf-8">
<title>Sing Along Harbor Weavers – Book Cover</title>
<link rel="stylesheet" href="https://fonts.googleapis.com/css2?family=Open+Sans:wght@400;700&display=swap">
<style>
  :root {
    --bg: #3a3238;
    --paper: #ffffff;
    --ink: #2a2a2a;
    --band: #111111;
    --accent-line: #c8b48a;
    --sky-top: #8a8f9a;
    --sky-mid: #e8a030;
    --sky-low: #f0901e;
    --ground: #1a1612;
    --white: #ffffff;
    --spine-grey: #d9d9d9;
  }
  * { box-sizing: border-box; margin: 0; padding: 0; }
  html, body { width: 1200px; height: 900px; overflow: hidden; }
  body {
    background: var(--bg);
    font-family: "Open Sans", Arial, sans-serif;
    color: var(--ink);
  }
  .book-spread {
    position: absolute;
    left: 173px; top: 140px;
    width: 854px; height: 620px;
    display: flex;
    box-shadow: 0 20px 50px rgba(0,0,0,.45);
  }

  /* Shared name lockup: plain text in the cover's text font */
  .brand-name {
    font-family: "Open Sans", Arial, sans-serif;
    font-weight: 700;
    color: var(--ink);
    line-height: 1.15;
  }

  /* Back cover */
  .back-cover {
    width: 400px; height: 620px;
    background: var(--paper);
    display: flex; flex-direction: column;
  }
  .back-body { padding: 38px 30px 0 30px; flex: 1; }
  .back-cover .brand-name { font-size: 24px; }
  .blurb { font-size: 9.5px; line-height: 1.45; margin-top: 30px; }
  .blurb p + p { margin-top: 12px; }
  .author-block { display: flex; gap: 14px; margin-top: 26px; align-items: flex-start; }
  .author-portrait {
    width: 62px; height: 62px; border-radius: 50%;
    background: radial-gradient(circle at 50% 40%, #d8c6b8, #5a6f9a 75%);
    border: 2px solid #7aa3d0; flex: none;
  }
  .author-name { font-size: 15px; font-weight: 700; margin-bottom: 6px; }
  .author-intro { font-size: 9.5px; line-height: 1.45; }
  .author-intro p + p { margin-top: 10px; }
  .author-story { font-size: 9.5px; line-height: 1.45; margin-top: 12px; }
  .back-band {
    height: 72px; background: var(--band);
    border-top: 4px solid var(--accent-line);
    display: flex; align-items: center; padding-left: 30px;
  }
  .site-address { color: var(--white); font-weight: 700; font-size: 12px; }

  /* Spine */
  .spine {
    width: 54px; height: 620px;
    background: var(--band);
    position: relative;
  }
  .spine-title, .spine-author {
    position: absolute; left: 50%;
    writing-mode: vertical-rl;
    transform: translateX(-50%);
    white-space: nowrap;
    color: var(--spine-grey);
  }
  .spine-title { top: 22px; font-size: 19px; font-weight: 700; letter-spacing: .5px; }
  .spine-divider { position: absolute; left: 12px; right: 12px; top: 446px; height: 1px; background: var(--spine-grey); }
  .spine-author { top: 462px; font-size: 14px; }

  /* Front cover */
  .front-cover {
    width: 400px; height: 620px;
    background: var(--paper);
    display: flex; flex-direction: column;
  }
  .cover-scene {
    height: 482px; position: relative;
    background: linear-gradient(180deg, var(--sky-top) 0%, #b8a27a 30%, var(--sky-mid) 55%, var(--sky-low) 72%, var(--ground) 78%, var(--ground) 100%);
  }
  .cover-author {
    position: absolute; top: 38px; right: 24px;
    color: var(--white); font-size: 22px; font-weight: 700;
  }
  .cover-quote {
    position: absolute; top: 150px; right: 22px; width: 180px;
    color: var(--white); font-size: 15px; font-weight: 700;
    line-height: 1.3; text-align: right;
  }
  .cover-brand {
    flex: 1;
    display: flex; align-items: center; justify-content: center;
    padding: 0 26px;
  }
  .front-cover .brand-name { font-size: 25px; text-align: center; }
</style>
</head>
<body>
  <main class="book-spread">
    <section class="back-cover">
      <div class="back-body">
        <div class="brand-name">Sing Along Harbor Weavers</div>
        <div class="blurb">
          <p>Now the Shale Energy Boom is right here in our backyard and we have decisions to make. Oil and Gas companies are exploring the Utica and other Shale formations in the eastern half of the state. Landmen have knocked on our door with lease offers, lawyers have researched whether our property is “held by production” from previous leases.</p>
          <p>Our neighbors have all called to discuss it, lawyers have invited us to landowner associations and we’ve been to township trustee meetings on the subject.</p>
        </div>
        <div class="author-block">
          <div class="author-portrait" role="img" aria-label="Round portrait photo of the author"></div>
          <div>
            <div class="author-name">Daniel H. Mercer</div>
            <div class="author-intro">
              <p>People often ask me how and why I got involved in the Sing Along Harbor Weavers Movement.</p>
              <p>So, I’m going to take a few minutes and share my story and introduce my “Big Why”. I’ll also share why I’m uniquely qualified to organize this project and what motivates me to help launch the Movement.</p>
            </div>
          </div>
        </div>
        <p class="author-story">As a child, I was fortunate enough to grow up and go to school in the south while spending my summers in Ohio. My father was a geologist for almost 50 years with his own oil and gas exploration company based in northern Louisiana.</p>
      </div>
      <div class="back-band"><span class="site-address">www.harborweavers.com</span></div>
    </section>

    <section class="spine">
      <span class="spine-title">Sing Along Harbor Weavers</span>
      <div class="spine-divider"></div>
      <span class="spine-author">Daniel H. Mercer</span>
    </section>

    <section class="front-cover">
      <div class="cover-scene" role="img" aria-label="Photograph of a drilling rig silhouetted against an orange sunset sky over flat land">
        <div class="cover-author">Daniel H. Mercer</div>
        <p class="cover-quote">"The Harbor Weavers are Empowering a Fresh and Different Kind of Environmental Movement"</p>
      </div>
      <div class="cover-brand">
        <div class="brand-name">Sing Along Harbor Weavers</div>
      </div>
    </section>
  </main>
</body>
</html>
```